Loan broker seeks referral card design for real estate financing

We need a design for a referral card for people who recommend us for real estate financing. If the deal goes through, each referrer will receive €750.

Text similar to: Recommend me! For every successful real estate financing referral, you will receive €750. (Other suggestions are also welcome)

The size should be no larger than A5 format, or possibly even oblong.
The design should convey security and competence and include themes such as independent advice.

The design should also include the company logo and a photo of me. Naturally, the design should also include a link to my website: www.die-brennholt.at, along with my phone number and email address: office@die-brennholt.at

```html
<!DOCTYPE html>
<html lang="en">
<head>
<meta charset="utf-8">
<title>Referral Card – Brennholt Finanz</title>
<link rel="stylesheet" href="https://fonts.googleapis.com/css2?family=Montserrat:wght@700&family=Source+Sans+3:wght@400;600&display=swap">
<style>
  :root {
    --stage: #b4b4b4;
    --brand-blue: #1a56b8;
    --white: #ffffff;
    --band-grey: #666666;
    --text-grey: #555555;
    --photo-dark: #3a2c28;
    --photo-mid: #6b5650;
  }
  * { box-sizing: border-box; margin: 0; padding: 0; }
  html, body { width: 1200px; height: 1027px; overflow: hidden; background: var(--stage); }
  .card {
    position: absolute; left: 91px; top: 155px; width: 1018px; height: 717px;
    background: var(--white); overflow: hidden;
    box-shadow: 0 3px 6px rgba(0,0,0,.25);
  }
  .offer-panel {
    position: absolute; left: 66px; top: 0; width: 492px; height: 548px;
    background: var(--brand-blue); border-radius: 0 0 30px 30px;
    color: var(--white); text-align: center;
    font-family: "Source Sans 3", sans-serif; font-weight: 600;
  }
  .headline {
    position: absolute; top: 44px; left: 0; width: 100%;
    font-family: "Montserrat", sans-serif; font-weight: 700; font-size: 45px; letter-spacing: .5px;
  }
  .offer-text {
    position: absolute; top: 107px; left: 0; width: 100%;
    font-size: 34px; line-height: 44px;
  }
  .amount-box {
    position: absolute; left: 19px; top: 252px; width: 454px; height: 148px;
    background: var(--white); border-radius: 15px;
    color: var(--brand-blue); font-family: "Montserrat", sans-serif; font-weight: 700;
    font-size: 140px; line-height: 148px; letter-spacing: -4px;
  }
  .welcome-lead { position: absolute; top: 420px; left: 0; width: 100%; font-size: 34px; }
  .welcome { position: absolute; top: 463px; left: 0; width: 100%; font-size: 54px; line-height: 64px; }
  .portrait {
    position: absolute; left: 558px; top: 0; width: 460px; height: 572px;
    background: linear-gradient(100deg, var(--photo-mid) 0%, var(--photo-dark) 55%, #2a2a3a 100%);
  }
  .contact-band {
    position: absolute; left: 0; top: 572px; width: 100%; height: 145px;
    background: var(--band-grey); color: var(--white); font-family: "Source Sans 3", sans-serif;
  }
  .phone {
    position: absolute; left: 0; width: 584px; top: 18px; text-align: center;
    font-family: "Montserrat", sans-serif; font-weight: 700; font-size: 52px;
  }
  .web-mail {
    position: absolute; left: 0; width: 584px; top: 84px; text-align: center;
    font-size: 27px; font-weight: 400;
  }
  .brand-area { position: absolute; left: 0; top: 572px; width: 100%; height: 145px; }
  .brand-name {
    position: absolute; left: 751px; top: 48px;
    font-family: "Source Sans 3", sans-serif; font-weight: 600; font-size: 21px; color: var(--brand-blue);
  }
  .brand-tagline {
    position: absolute; left: 751px; top: 74px;
    font-family: "Source Sans 3", sans-serif; font-weight: 600; font-size: 15px; color: var(--text-grey);
  }
</style>
</head>
<body>
  <div class="card">
    <div class="portrait" role="img" aria-label="Portrait photo of the advisor in a dark suit and white shirt"></div>

    <div class="offer-panel">
      <h1 class="headline">Recommend me!</h1>
      <p class="offer-text">For every successful<br>real estate financing referral<br>you will receive</p>
      <div class="amount-box">€750</div>
      <p class="welcome-lead">Other suggestions are also</p>
      <p class="welcome">WELCOME</p>
    </div>

    <div class="contact-band">
      <p class="phone">+43 660 214 5837</p>
      <p class="web-mail">www.die-brennholt.at &nbsp;|&nbsp; office@die-brennholt.at</p>
    </div>

    <div class="brand-area">
      <svg width="1018" height="145" style="position:absolute;left:0;top:0">
        <polygon points="641,6 1018,6 1018,145 566,145" fill="var(--white)"/>
        <circle cx="683" cy="73" r="47" fill="none" stroke="var(--brand-blue)" stroke-width="4"/>
        <line x1="742" y1="25" x2="742" y2="120" stroke="var(--text-grey)" stroke-width="2"/>
      </svg>
      <p class="brand-name">Brennholt Finanz GmbH</p>
      <p class="brand-tagline">Finanzieren, Versichern, Vorsorgen</p>
    </div>
  </div>
</body>
</html>
```